business card for author of crime novel

I am an author with a new book. I need a business card with the book's cover on one side (already uploaded), and contact details on the other.

Walt Pemberty
Author

telephone: 646-512-7380
website: www.waltpemberty.net
facebook: folioreads.net/wpemberty
twitter: chatterline.net/wpemberty
email: wpemberty@postvale.net

Target Market(s)

Readers of mystery books

Industry/Entity Type

Business

Contact Information for Business Card

Walt Pemberty
Author

telephone: 646-512-7380

Font styles to use
Serif
Sans Serif

Requirements
Must have
• Book cover on one side. My contact info on the other, with the name of the book repeated if that makes sense. Clean design.
Should not have
• Overly ornate, too formal, too distracting

```html
<!DOCTYPE html>
<html lang="en">
<head>
<meta charset="utf-8">
<title>Walt Pemberty — Business Card</title>
<link rel="stylesheet" href="https://fonts.googleapis.com/css2?family=Libre+Baskerville:wght@400;700&family=Open+Sans:wght@700&family=Tinos:wght@400;700&display=swap">
<style>
  :root {
    --gold: #e3c23a;
    --gold-deep: #c9a21f;
    --gold-light: #f1d960;
    --ink: #0b0b0b;
    --stage: #e9e5dc;
    --cover-dark: #3e5966;
    --cover-light: #a9c4cd;
    --label: #ece5cf;
    --label-ink: #2a2620;
  }
  * { margin: 0; padding: 0; box-sizing: border-box; }
  html, body { width: 1200px; height: 892px; overflow: hidden; }
  body {
    background: var(--stage);
    position: relative;
    font-family: "Tinos", "Times New Roman", serif;
  }
  .card {
    position: absolute;
    top: 106px;
    width: 380px;
    height: 680px;
    overflow: hidden;
    box-shadow: 0 8px 24px rgba(0,0,0,.25);
  }
  /* Contact side */
  .card-front { left: 190px; background: var(--ink); }
  .band { position: absolute; left: 0; right: 0; background: linear-gradient(90deg, var(--gold-deep), var(--gold-light), var(--gold-deep)); }
  .band-top { top: 0; height: 44px; }
  .band-bottom { bottom: 0; height: 56px; }
  .masthead { position: absolute; top: 92px; left: 24px; right: 24px; }
  .masthead-name {
    font-family: "Libre Baskerville", Georgia, serif;
    font-weight: 700; font-size: 36px; color: var(--gold); line-height: 1;
    white-space: nowrap; text-align: right; letter-spacing: -.5px;
  }
  .masthead-sub { display: flex; align-items: center; gap: 8px; margin-top: 6px; }
  .masthead-rule { flex: 1; height: 2px; background: var(--gold-deep); }
  .masthead-series {
    font-family: "Open Sans", Arial, sans-serif; font-weight: 700; font-size: 11px;
    color: var(--gold); letter-spacing: .3px; white-space: nowrap;
  }
  .identity { position: absolute; top: 236px; right: 40px; text-align: right; color: var(--gold); }
  .identity-name { font-weight: 700; font-size: 32px; line-height: 1.05; font-family: "Libre Baskerville", Georgia, serif; white-space: nowrap; }
  .identity-role { font-size: 20px; margin-top: 4px; }
  .contacts { position: absolute; top: 382px; right: 30px; list-style: none; }
  .contact { display: flex; justify-content: flex-end; align-items: center; gap: 12px; height: 36px; color: var(--gold); font-size: 21px; white-space: nowrap; }
  .contact-icon { width: 22px; height: 22px; background: var(--gold); border-radius: 3px; display: flex; align-items: center; justify-content: center; flex: none; }
  .contact-icon svg { width: 14px; height: 14px; }

  /* Cover side */
  .card-back { left: 630px; background: linear-gradient(160deg, var(--gold-light), var(--gold) 45%, var(--gold-deep)); }
  .cover {
    position: absolute; top: 48px; left: 30px; right: 30px; height: 440px;
    background: linear-gradient(165deg, var(--cover-light), #7b9aa6 45%, var(--cover-dark));
    box-shadow: 0 2px 6px rgba(0,0,0,.3);
  }
  .cover-author {
    position: absolute; right: 24px; bottom: 46px; text-align: right;
    font-family: "Tinos", serif; font-size: 28px; line-height: 1.05; color: var(--gold-light); letter-spacing: 1px;
  }
  .cover-label {
    position: absolute; left: 30px; right: 22px; top: 482px; height: 56px;
    background: var(--label); border-radius: 3px; box-shadow: 0 2px 4px rgba(0,0,0,.3);
    display: flex; align-items: center; justify-content: center;
    font-family: "Tinos", serif; font-size: 27px; color: var(--label-ink);
  }
  .url-band {
    position: absolute; left: 0; right: 0; bottom: 0; height: 96px; background: var(--ink);
    display: flex; align-items: center; justify-content: center;
    font-family: "Libre Baskerville", Georgia, serif; font-weight: 700; font-size: 22px; color: var(--gold);
  }
</style>
</head>
<body>
  <article class="card card-front">
    <div class="band band-top"></div>
    <header class="masthead">
      <h1 class="masthead-name">Walt Pemberty</h1>
      <div class="masthead-sub">
        <div class="masthead-rule"></div>
        <p class="masthead-series">Author of the Harlan Voss Mysteries</p>
      </div>
    </header>
    <div class="identity">
      <p class="identity-name">Walt Pemberty</p>
      <p class="identity-role">Author</p>
    </div>
    <ul class="contacts">
      <li class="contact">646-512-7380
        <span class="contact-icon"><svg viewBox="0 0 16 16"><path d="M3 1l3 3-1.5 2c1 2 3 4 5 5L11.5 9.5l3 3-2 2.5C7 14 2 9 1 3.5z" fill="#0b0b0b"/></svg></span></li>
      <li class="contact">wpemberty@postvale.net
        <span class="contact-icon"><svg viewBox="0 0 16 16"><rect x="1" y="3" width="14" height="10" fill="none" stroke="#0b0b0b" stroke-width="1.6"/><path d="M1 3l7 6 7-6" fill="none" stroke="#0b0b0b" stroke-width="1.6"/></svg></span></li>
      <li class="contact">www.waltpemberty.net
        <span class="contact-icon"><svg viewBox="0 0 16 16"><circle cx="8" cy="8" r="6.5" fill="none" stroke="#0b0b0b" stroke-width="1.5"/><ellipse cx="8" cy="8" rx="3" ry="6.5" fill="none" stroke="#0b0b0b" stroke-width="1.2"/><path d="M1.5 8h13" stroke="#0b0b0b" stroke-width="1.2"/></svg></span></li>
      <li class="contact">folioreads.net/wpemberty
        <span class="contact-icon"></span></li>
      <li class="contact">chatterline.net/wpemberty
        <span class="contact-icon"></span></li>
    </ul>
    <div class="band band-bottom"></div>
  </article>

  <article class="card card-back">
    <div class="cover" role="img" aria-label="Book cover photograph of an old city apartment building with fire escapes, in cold blue tones">
      <p class="cover-author">WALT<br>PEMBERTY</p>
    </div>
    <div class="cover-label">A Harlan Voss Mystery</div>
    <footer class="url-band">www.waltpemberty.net</footer>
  </article>
</body>
</html>
```